Business Card Design

We service, sell & install vehicle hoists in automotive workshops & would like the colours royal blue or green incorporated into the design.

Industry/Entity Type

Automotive

Contact Information for Business Card

KTL Lifts
Equipment Sales & Service
Colin Marwick 0412 781 359
Dean Corbett 0417 925 163
14 Lyall Street Kyneton Vic 3444
email: ktllifts@mailbox.example.au

```html
<!DOCTYPE html>
<html lang="en">
<head>
<meta charset="utf-8">
<title>KTL Lifts – Business Card</title>
<link rel="stylesheet" href="https://fonts.googleapis.com/css2?family=Open+Sans:wght@300;400;700&display=swap">
<style>
  :root {
    --backdrop: #262626;
    --card: #151515;
    --card-edge: #2e2e2e;
    --text: #e8e8e8;
    --text-soft: #d4d4d4;
    --royal-blue: #3a66e0;
  }
  html, body {
    margin: 0;
    width: 1200px;
    height: 938px;
    overflow: hidden;
    background: var(--backdrop);
  }
  .card {
    position: absolute;
    left: 255px;
    top: 253px;
    width: 693px;
    height: 430px;
    background: var(--card);
    border: 1px solid var(--card-edge);
    box-sizing: border-box;
    font-family: "Open Sans", Arial, sans-serif;
    color: var(--text);
    text-align: center;
  }
  .brand-mark {
    position: absolute;
    top: 40px;
    left: 0;
    right: 0;
    font-size: 66px;
    font-weight: 700;
    line-height: 1;
    letter-spacing: -2px;
    color: var(--royal-blue);
  }
  .brand-name {
    position: absolute;
    top: 111px;
    left: 0;
    right: 0;
    font-size: 32px;
    font-weight: 300;
    line-height: 1.1;
    color: var(--text);
  }
  .brand-tagline {
    position: absolute;
    top: 150px;
    left: 0;
    right: 0;
    font-size: 20px;
    font-weight: 300;
    color: var(--text-soft);
  }
  .person {
    position: absolute;
    top: 229px;
    left: 0;
    right: 0;
    font-size: 30px;
    font-weight: 300;
    letter-spacing: 0.5px;
    text-transform: uppercase;
  }
  .person strong { font-weight: 700; }
  .contact {
    position: absolute;
    top: 329px;
    left: 0;
    right: 0;
    font-size: 19px;
    font-weight: 300;
    line-height: 30px;
    text-transform: uppercase;
    color: var(--text-soft);
  }
  .contact b { font-weight: 700; color: var(--royal-blue); }
  .contact p { margin: 0; }
</style>
</head>
<body>
  <div class="card">
    <div class="brand-mark">KTL</div>
    <div class="brand-name">Lifts Equipment</div>
    <div class="brand-tagline">Sales &amp; Service</div>
    <div class="person">Dean <strong>Corbett</strong></div>
    <div class="contact">
      <p class="address">14 Lyall Street Kyneton Vic 3444</p>
      <p class="lines"><b>C.</b> 0417 925 163 | <b>E.</b> ktllifts@mailbox.example.au</p>
    </div>
  </div>
</body>
</html>
```